Reproduce my app screenshot to look more updated and modern

My app is a place for farmers to post jobs a when needing help around the Farm, and local farmhands can apply for the job. The Farmer can then review multiple applicants and select the one best fit for the task at hand. I'm trying to give my screens an updated look while keeping my current color scheme and flow. I would like for you guys to recreate this screen with an updated loo the best you can. The main screen with the TW will stay the same. I put that in there to show our logo and our main colors. They look outdated.

Target Market(s)

Farmers and Farm Emlpoyees inside the US

Industry/Entity Type

Agriculture

Requirements
Must have
• and updated look and same buttom/ functionality
Nice to have
Should not have
• dont change the name of any buttons

```html
<!DOCTYPE html>
<html lang="en">
<head>
<meta charset="utf-8">
<title>Current Jobs For You</title>
<link href="https://fonts.googleapis.com/css2?family=Inter:wght@400;500;600;700&display=swap" rel="stylesheet">
<style>
  :root {
    --green: #76a84c;
    --green-dark: #5f9139;
    --green-light: #8cbd5c;
    --lime: #c6ec7e;
    --ink: #1f1f1f;
    --ink-soft: #444;
    --muted: #8d8d8d;
    --faint: #c7c7c7;
    --panel: #f4f4f4;
    --card: #ffffff;
    --page: #ececec;
    --heart: #ef3b3b;
    --orange: #f19444; --orange-bg: #fef3ea;
    --blue: #3b98e0;   --blue-bg: #eef6fd;
    --leaf: #79b548;   --leaf-bg: #f1f7ec;
    --violet: #5546b6; --violet-bg: #efeef8;
    --yellow: #d8d027; --yellow-bg: #fbfbe5;
  }
  * { box-sizing: border-box; margin: 0; padding: 0; }
  html, body { width: 787px; height: 1200px; overflow: hidden; }
  body { background: var(--page); font-family: "Inter", sans-serif; color: var(--ink); position: relative; }

  .screen {
    position: absolute; left: 116px; top: 0; width: 555px; height: 1200px;
    background: var(--panel); border-radius: 40px; overflow: hidden;
  }
  .header {
    position: absolute; left: 0; top: 0; width: 100%; height: 200px;
    background: linear-gradient(120deg, var(--green-dark), var(--green) 55%, var(--green-light));
  }
  .avatar {
    position: absolute; left: 30px; top: 78px; width: 56px; height: 56px; border-radius: 50%;
    background: radial-gradient(circle at 50% 40%, #d9d9d9, #8a8a8a);
    border: 3px solid rgba(255,255,255,.85);
    box-shadow: 0 4px 10px rgba(0,0,0,.25);
  }
  .profile { position: absolute; left: 100px; top: 88px; color: #fff; }
  .profile-name { font-size: 23px; font-weight: 700; letter-spacing: -.3px; line-height: 1; }
  .profile-phone { font-size: 16px; font-weight: 400; margin-top: 5px; }
  .header-actions { position: absolute; top: 91px; left: 404px; display: flex; align-items: center; gap: 24px; }
  .add-btn { width: 28px; height: 28px; border-radius: 50%; background: #fff; display: flex; align-items: center; justify-content: center; }
  .bell { position: relative; }
  .bell-dot { position: absolute; right: 1px; top: 0; width: 6px; height: 6px; background: var(--heart); border-radius: 50%; }

  .panel {
    position: absolute; left: 0; top: 161px; width: 100%; height: 1039px;
    background: var(--panel); border-radius: 49px 49px 0 0;
  }
  .tabs { position: absolute; top: 30px; left: 78px; display: flex; gap: 37px; font-size: 19px; font-weight: 600; letter-spacing: -.3px; white-space: nowrap; }
  .tab { color: var(--faint); }
  .tab.is-active { color: var(--ink); position: relative; }
  .tab.is-active::after { content: ""; position: absolute; left: 31px; top: 39px; width: 111px; height: 5px; border-radius: 3px; background: var(--green-light); }

  .search {
    position: absolute; left: 24px; top: 101px; width: 461px; height: 59px; border-radius: 30px;
    background: #fff; display: flex; align-items: center; padding-left: 21px; gap: 10px;
    font-size: 19px; color: var(--faint);
  }
  .filter-btn { position: absolute; left: 502px; top: 115px; }

  .job-list { position: absolute; left: 24px; top: 196px; width: 507px; }
  .job-card {
    position: relative; height: 123px; margin-bottom: 26px; background: var(--card);
    border-radius: 16px; box-shadow: 0 3px 12px rgba(0,0,0,.04);
  }
  .date-box {
    position: absolute; left: 13px; top: 13px; width: 97px; height: 97px; border-radius: 16px;
    display: flex; flex-direction: column; justify-content: center; padding-left: 20px;
    font-size: 17px; font-weight: 600; line-height: 1; white-space: nowrap;
  }
  .date-to { font-size: 11px; margin: 8px 0; display: flex; align-items: center; gap: 2px; }
  .date-to::before, .date-to::after { content: ""; width: 16px; height: 1px; background: currentColor; }
  .date-box.orange { color: var(--orange); background: var(--orange-bg); }
  .date-box.blue { color: var(--blue); background: var(--blue-bg); }
  .date-box.leaf { color: var(--leaf); background: var(--leaf-bg); }
  .date-box.violet { color: var(--violet); background: var(--violet-bg); }
  .date-box.yellow { color: var(--yellow); background: var(--yellow-bg); }

  .job-info { position: absolute; left: 125px; top: 19px; width: 268px; }
  .job-title { font-size: 16px; font-weight: 400; color: var(--ink); letter-spacing: -.35px; line-height: 20px; margin-bottom: 3px; white-space: nowrap; }
  .job-meta { font-size: 14px; color: var(--muted); display: flex; align-items: center; gap: 5px; height: 22px; white-space: nowrap; }
  .job-meta svg { flex: none; }

  .job-pay { position: absolute; left: 391px; top: 40px; width: 108px; }
  .pay-rate { font-size: 26px; font-weight: 700; color: var(--ink-soft); letter-spacing: -.5px; line-height: 1; white-space: nowrap; }
  .pay-label { font-size: 14px; color: var(--muted); margin-top: 6px; padding-left: 10px; white-space: nowrap; }
  .fav { position: absolute; right: 14px; top: 9px; }

  .tab-bar {
    position: absolute; left: 0; top: 1086px; width: 100%; height: 114px;
    background: #fff; border-radius: 30px 30px 0 0; box-shadow: 0 -4px 14px rgba(0,0,0,.03);
  }
  .nav-item { position: absolute; top: 17px; width: 53px; height: 53px; display: flex; align-items: center; justify-content: center; }
  .nav-item.is-active { background: var(--lime); border-radius: 50%; }
  .home-indicator { position: absolute; left: 183px; bottom: 12px; width: 188px; height: 6px; border-radius: 3px; background: #111; }
</style>
</head>
<body>
<main class="screen">
  <header class="header">
    <div class="avatar" role="img" aria-label="Profile photo of Daniel Harlow"></div>
    <div class="profile">
      <div class="profile-name">Daniel Harlow</div>
      <div class="profile-phone">5550142876</div>
    </div>
    <div class="header-actions">
      <span class="add-btn"><svg width="12" height="12" viewBox="0 0 12 12"><path d="M6 1v10M1 6h10" stroke="var(--green)" stroke-width="1.8" stroke-linecap="round"/></svg></span>
      <span class="bell"><svg width="24" height="26" viewBox="0 0 24 26" fill="none" stroke="#fff" stroke-width="1.6" stroke-linejoin="round"><path d="M5 19V11a7 7 0 0 1 14 0v8l2 2H3z"/><path d="M10 23a2 2 0 0 0 4 0"/></svg><span class="bell-dot"></span></span>
      <svg width="24" height="14" viewBox="0 0 24 14"><path d="M1 2h22M8 12h15" stroke="#fff" stroke-width="2" stroke-linecap="round"/></svg>
    </div>
  </header>

  <section class="panel">
    <nav class="tabs">
      <span class="tab is-active">Current Jobs For You</span>
      <span class="tab">Nearby Farmhands</span>
    </nav>

    <div class="search">
      <svg width="17" height="17" viewBox="0 0 17 17" fill="none" stroke="#b5b5b5" stroke-width="1.5"><circle cx="7" cy="7" r="6"/><path d="M11.5 11.5l4.5 4.5" stroke-linecap="round"/></svg>
      Search
    </div>
    <span class="filter-btn"><svg width="28" height="28" viewBox="0 0 28 28" fill="none" stroke="var(--green-dark)" stroke-width="1.3"><path d="M1 5h26M1 14h26M1 23h26"/><rect x="7" y="2" width="4" height="6" fill="#f4f4f4"/><rect x="16" y="11" width="4" height="6" fill="#f4f4f4"/><rect x="7" y="20" width="4" height="6" fill="#f4f4f4"/></svg></span>

    <div class="job-list">
      <article class="job-card">
        <div class="date-box orange"><span>01 APR</span><span class="date-to">TO</span><span>15 APR</span></div>
        <div class="job-info">
          <h3 class="job-title">Seasonal Farm Labor</h3>
          <p class="job-meta"><svg width="7" height="9" viewBox="0 0 7 9"><path d="M3.5 0A3.5 3.5 0 0 0 0 3.5C0 6 3.5 9 3.5 9S7 6 7 3.5A3.5 3.5 0 0 0 3.5 0z" fill="#aaa"/></svg>Dewitt, Lowa</p>
          <p class="job-meta"><svg width="8" height="7" viewBox="0 0 8 7"><path d="M2 0L0 7h3l1-3 1 3h3L6 0z" fill="#aaa"/></svg>2.92 miles</p>
          <p class="job-meta"><svg width="8" height="8" viewBox="0 0 8 8"><circle cx="4" cy="4" r="4" fill="#aaa"/><path d="M4 2v2h2" stroke="#fff" stroke-width="1"/></svg>08:00 am - 08:00 pm</p>
        </div>
        <div class="job-pay"><div class="pay-rate">$12-20</div><div class="pay-label">Hourly Rate</div></div>
        <svg class="fav" width="19" height="17" viewBox="0 0 24 21"><path d="M12 21L2 11a6 6 0 0 1 10-7 6 6 0 0 1 10 7z" fill="var(--heart)"/></svg>
      </article>

      <article class="job-card">
        <div class="date-box blue"><span>01 MAR</span><span class="date-to">TO</span><span>02 MAR</span></div>
        <div class="job-info">
          <h3 class="job-title">Truck Driver</h3>
          <p class="job-meta"><svg width="7" height="9" viewBox="0 0 7 9"><path d="M3.5 0A3.5 3.5 0 0 0 0 3.5C0 6 3.5 9 3.5 9S7 6 7 3.5A3.5 3.5 0 0 0 3.5 0z" fill="#aaa"/></svg>Davenport, Lowa</p>
          <p class="job-meta"><svg width="8" height="7" viewBox="0 0 8 7"><path d="M2 0L0 7h3l1-3 1 3h3L6 0z" fill="#aaa"/></svg>12.38 miles</p>
          <p class="job-meta"><svg width="8" height="8" viewBox="0 0 8 8"><circle cx="4" cy="4" r="4" fill="#aaa"/><path d="M4 2v2h2" stroke="#fff" stroke-width="1"/></svg>10:00 am - 03:00 pm</p>
        </div>
        <div class="job-pay"><div class="pay-rate">$15-25</div><div class="pay-label">Hourly Rate</div></div>
        <svg class="fav" width="19" height="17" viewBox="0 0 24 21"><path d="M12 20L2.5 10.5a5.5 5.5 0 0 1 9.5-6 5.5 5.5 0 0 1 9.5 6z" fill="none" stroke="#ccc" stroke-width="1.4"/></svg>
      </article>

      <article class="job-card">
        <div class="date-box leaf"><span>31 JAN</span><span class="date-to">TO</span><span>25 FEB</span></div>
        <div class="job-info">
          <h3 class="job-title">Farm Hand, Sprayer, Truck, Repair</h3>
          <p class="job-meta"><svg width="7" height="9" viewBox="0 0 7 9"><path d="M3.5 0A3.5 3.5 0 0 0 0 3.5C0 6 3.5 9 3.5 9S7 6 7 3.5A3.5 3.5 0 0 0 3.5 0z" fill="#aaa"/></svg>Dewitt, Lowa</p>
          <p class="job-meta"><svg width="8" height="7" viewBox="0 0 8 7"><path d="M2 0L0 7h3l1-3 1 3h3L6 0z" fill="#aaa"/></svg>2.92 miles</p>
          <p class="job-meta"><svg width="8" height="8" viewBox="0 0 8 8"><circle cx="4" cy="4" r="4" fill="#aaa"/><path d="M4 2v2h2" stroke="#fff" stroke-width="1"/></svg>10:00 am - 05:00 pm</p>
        </div>
        <div class="job-pay"><div class="pay-rate">$17-22</div><div class="pay-label">Hourly Rate</div></div>
        <svg class="fav" width="19" height="17" viewBox="0 0 24 21"><path d="M12 20L2.5 10.5a5.5 5.5 0 0 1 9.5-6 5.5 5.5 0 0 1 9.5 6z" fill="none" stroke="#ddd" stroke-width="1.4"/></svg>
      </article>

      <article class="job-card">
        <div class="date-box violet"><span>27 MAR</span><span class="date-to">TO</span><span>27 MAR</span></div>
        <div class="job-info">
          <h3 class="job-title">Sort and Load Pigs</h3>
          <p class="job-meta"><svg width="7" height="9" viewBox="0 0 7 9"><path d="M3.5 0A3.5 3.5 0 0 0 0 3.5C0 6 3.5 9 3.5 9S7 6 7 3.5A3.5 3.5 0 0 0 3.5 0z" fill="#aaa"/></svg>Dewitt, Lowa</p>
          <p class="job-meta"><svg width="8" height="7" viewBox="0 0 8 7"><path d="M2 0L0 7h3l1-3 1 3h3L6 0z" fill="#aaa"/></svg>2.92 miles</p>
          <p class="job-meta"><svg width="8" height="8" viewBox="0 0 8 8"><circle cx="4" cy="4" r="4" fill="#aaa"/><path d="M4 2v2h2" stroke="#fff" stroke-width="1"/></svg>08:00 am - 08:00 pm</p>
        </div>
        <div class="job-pay"><div class="pay-rate">$10-20</div><div class="pay-label">Hourly Rate</div></div>
        <svg class="fav" width="19" height="17" viewBox="0 0 24 21"><path d="M12 21L2 11a6 6 0 0 1 10-7 6 6 0 0 1 10 7z" fill="var(--heart)"/></svg>
      </article>

      <article class="job-card">
        <div class="date-box yellow"><span>13 JUL</span><span class="date-to">TO</span><span>14 JUL</span></div>
        <div class="job-info">
          <h3 class="job-title">Need Help Bailing Hay, small squares</h3>
          <p class="job-meta"><svg width="7" height="9" viewBox="0 0 7 9"><path d="M3.5 0A3.5 3.5 0 0 0 0 3.5C0 6 3.5 9 3.5 9S7 6 7 3.5A3.5 3.5 0 0 0 3.5 0z" fill="#aaa"/></svg>Alabaster, Alabama</p>
          <p class="job-meta"><svg width="8" height="7" viewBox="0 0 8 7"><path d="M2 0L0 7h3l1-3 1 3h3L6 0z" fill="#aaa"/></svg>5118 miles</p>
          <p class="job-meta"><svg width="8" height="8" viewBox="0 0 8 8"><circle cx="4" cy="4" r="4" fill="#aaa"/><path d="M4 2v2h2" stroke="#fff" stroke-width="1"/></svg>06:00 am - 05:00 pm</p>
        </div>
        <div class="job-pay"><div class="pay-rate">$20-25</div><div class="pay-label">Hourly Rate</div></div>
        <svg class="fav" width="19" height="17" viewBox="0 0 24 21"><path d="M12 20L2.5 10.5a5.5 5.5 0 0 1 9.5-6 5.5 5.5 0 0 1 9.5 6z" fill="none" stroke="#ddd" stroke-width="1.4"/></svg>
      </article>
    </div>
  </section>

  <nav class="tab-bar">
    <span class="nav-item is-active" style="left:42px"><svg width="28" height="26" viewBox="0 0 28 26" fill="none" stroke="#2d4a1c" stroke-width="1.8" stroke-linejoin="round"><path d="M2 12L14 2l12 10"/><path d="M5 10v14h18V10"/><path d="M11 24v-8h6v8" fill="#5f9139"/></svg></span>
    <span class="nav-item" style="left:150px"><svg width="26" height="26" viewBox="0 0 26 26" fill="none" stroke="#aaa" stroke-width="1.5"><circle cx="10" cy="10" r="8"/><circle cx="10" cy="10" r="5"/><path d="M16 16l8 8" stroke-linecap="round" stroke-width="2.5"/></svg></span>
    <span class="nav-item" style="left:256px"><svg width="26" height="26" viewBox="0 0 26 26" fill="none" stroke="#aaa" stroke-width="1.5"><rect x="1" y="2" width="24" height="22" rx="3"/><path d="M1 7h24M6 12h14M6 16h14M6 20h8"/></svg></span>
    <span class="nav-item" style="left:359px"><svg width="24" height="28" viewBox="0 0 24 28" fill="none" stroke="#aaa" stroke-width="1.4" stroke-linecap="round" stroke-linejoin="round"><path d="M7 14V5a1.5 1.5 0 0 1 3 0v8V3a1.5 1.5 0 0 1 3 0v10V4a1.5 1.5 0 0 1 3 0v10V7a1.5 1.5 0 0 1 3 0v11c0 5-3 8-7 8s-6-2-8-6l-3-5a1.5 1.5 0 0 1 2.5-1.5L7 16"/></svg></span>
    <span class="nav-item" style="left:461px"><svg width="26" height="26" viewBox="0 0 26 26" fill="none" stroke="#aaa" stroke-width="1.5"><rect x="1" y="4" width="24" height="21" rx="3"/><path d="M1 10h24M7 1v5M19 1v5"/><path d="M7 15h1M12 15h1M17 15h1M7 20h1M12 20h1M17 20h1" stroke-width="2" stroke-linecap="round"/></svg></span>
    <span class="home-indicator"></span>
  </nav>
</main>
</body>
</html>
```